Brinmoor Export Partners, LLC
Business cards and stationery
Brinmoor Export Partners, LLC -
Creative Brief
Simple
Dalton (Skip) Harrow
President/CEO
2274 Fennick Lane Round Rock, TX 78664
skip@brinmoorexport.example
www.brinmoorexport.example
We are a US based start up company that identifies market opportunities and procures private label products for export to international markets, initially with first to market products. Brinmoor Export Partners is commited to Operating with honesty and integrity Professional, dependable customer service Flexibility in meeting customer needs without compromising values Friendly, laid-back, relational business style (Austin vs. NYC) Focus on family, people and relationships while getting the job done High standards for choosing quality products
We would like a QR code with the contact information that is listed on the front of the card.

```html
<!DOCTYPE html>
<html lang="en">
<head>
<meta charset="utf-8">
<title>Brinmoor Export Partners, LLC – Business Cards</title>
<link href="https://fonts.googleapis.com/css2?family=Open+Sans:wght@400;600;700;800&display=swap" rel="stylesheet">
<style>
  :root {
    --bg: #3a3a3a;
    --card: #ffffff;
    --red: #c8102e;
    --ink: #2b2b2b;
    --muted: #555555;
    --rule: #9a9a9a;
  }
  * { box-sizing: border-box; margin: 0; padding: 0; }
  html, body { width: 1200px; height: 852px; overflow: hidden; }
  body {
    background: var(--bg);
    font-family: "Open Sans", Arial, sans-serif;
    color: var(--ink);
    position: relative;
  }
  .card {
    position: absolute;
    width: 700px;
    height: 400px;
    background: var(--card);
    border-radius: 22px;
    overflow: hidden;
    box-shadow: 0 10px 24px rgba(0,0,0,.45);
  }
  .card--front { left: 110px; top: 16px; }
  .card--alt { left: 390px; top: 436px; }
  .card .swoosh { position: absolute; inset: 0; width: 100%; height: 100%; }

  .brand { position: absolute; }
  .brand__name { display: block; font-weight: 800; color: var(--ink); line-height: 1.08; }

  .card--front .brand { left: 44px; top: 158px; width: 290px; text-align: center; }
  .card--front .brand__name { font-size: 32px; }

  .divider { position: absolute; width: 1px; background: var(--rule); }
  .card--front .divider { left: 352px; top: 70px; height: 260px; }

  .person__name { color: var(--red); font-weight: 700; font-size: 21px; }
  .person__title { font-weight: 700; font-size: 14px; color: var(--ink); margin-top: 2px; }
  .address { font-size: 14px; color: var(--muted); line-height: 1.45; }
  .contacts { list-style: none; font-size: 14px; color: var(--muted); }
  .contacts li { display: flex; align-items: center; gap: 9px; line-height: 1.75; }
  .contacts svg { width: 13px; height: 13px; flex: none; }

  .card--front .details { position: absolute; left: 372px; top: 72px; }
  .card--front .address { margin-top: 40px; }
  .card--front .contacts { margin-top: 26px; }

  .card--alt .brand { left: 130px; top: 76px; width: 460px; text-align: center; }
  .card--alt .brand__name { font-size: 42px; }
  .card--alt .details-left { position: absolute; right: 372px; top: 250px; text-align: right; }
  .card--alt .address { margin-top: 12px; }
  .card--alt .divider { left: 345px; top: 248px; height: 110px; }
  .card--alt .contacts { position: absolute; left: 362px; top: 256px; }
</style>
</head>
<body>

<article class="card card--front" aria-label="Business card, front layout">
  <svg class="swoosh" viewBox="0 0 700 400" preserveAspectRatio="none" aria-hidden="true">
    <path d="M0 0 H250 C160 20 60 80 0 210 Z" fill="var(--red)"/>
    <path d="M250 0 C160 20 60 80 0 210 V225 C60 95 165 30 290 0 Z" fill="var(--ink)"/>
    <path d="M700 400 H450 C540 380 640 320 700 190 Z" fill="var(--red)"/>
    <path d="M450 400 C540 380 640 320 700 190 V175 C640 305 535 370 410 400 Z" fill="var(--ink)"/>
  </svg>
  <div class="brand">
    <span class="brand__name">Brinmoor Export Partners</span>
  </div>
  <div class="divider"></div>
  <div class="details">
    <p class="person__name">Dalton (Skip) Harrow</p>
    <p class="person__title">President/CEO</p>
    <p class="address">2274 Fennick Lane<br>Round Rock, TX 78664</p>
    <ul class="contacts">
      <li><svg viewBox="0 0 16 16"><path d="M4 1l3 3-2 2c1 2 3 4 5 5l2-2 3 3-2 3C7 14 2 9 1 3z" fill="var(--red)"/></svg>(512) 555-0147</li>
      <li><svg viewBox="0 0 16 16"><circle cx="8" cy="8" r="7" fill="var(--red)"/><rect x="4" y="5" width="8" height="6" fill="#fff"/></svg>skip@brinmoorexport.example</li>
      <li><svg viewBox="0 0 16 16"><circle cx="8" cy="8" r="7" fill="var(--red)"/><circle cx="8" cy="8" r="3.5" fill="none" stroke="#fff" stroke-width="1.4"/></svg>www.brinmoorexport.example</li>
    </ul>
  </div>
</article>

<article class="card card--alt" aria-label="Business card, alternate layout">
  <svg class="swoosh" viewBox="0 0 700 400" preserveAspectRatio="none" aria-hidden="true">
    <path d="M0 0 H170 C100 15 40 55 0 130 Z" fill="var(--red)"/>
    <path d="M170 0 C100 15 40 55 0 130 V142 C45 65 110 22 200 0 Z" fill="var(--ink)"/>
    <path d="M700 20 C655 130 650 280 700 400 Z" fill="var(--ink)"/>
    <path d="M700 60 C670 150 668 270 700 370 Z" fill="var(--red)"/>
  </svg>
  <div class="brand">
    <span class="brand__name">Brinmoor Export<br>Partners</span>
  </div>
  <div class="details-left">
    <p class="person__name">Dalton (Skip) Harrow</p>
    <p class="person__title">President/CEO</p>
    <p class="address">2274 Fennick Lane<br>Round Rock, TX 78664</p>
  </div>
  <div class="divider"></div>
  <ul class="contacts">
    <li><svg viewBox="0 0 16 16"><path d="M4 1l3 3-2 2c1 2 3 4 5 5l2-2 3 3-2 3C7 14 2 9 1 3z" fill="var(--red)"/></svg>(512) 555-0147</li>
    <li><svg viewBox="0 0 16 16"><circle cx="8" cy="8" r="7" fill="var(--red)"/><rect x="4" y="5" width="8" height="6" fill="#fff"/></svg>skip@brinmoorexport.example</li>
    <li><svg viewBox="0 0 16 16"><circle cx="8" cy="8" r="7" fill="var(--red)"/><circle cx="8" cy="8" r="3.5" fill="none" stroke="#fff" stroke-width="1.4"/></svg>www.brinmoorexport.example</li>
  </ul>
</article>

</body>
</html>
```